Business Card Design

Needing a business card design similar to the business card that is attached.

Industry/Entity Type

Business

Contact Information for Business Card

Design similar to the b-cards that is attached.

```html
<!DOCTYPE html>
<html lang="en">
<head>
<meta charset="utf-8">
<title>Business Cards</title>
<link rel="stylesheet" href="https://fonts.googleapis.com/css2?family=Tinos:ital,wght@0,400;0,700;1,400&display=swap">
<style>
  :root {
    --backdrop: #e4e4e4;
    --card: #ffffff;
    --ink: #1a1a1a;
    --accent-red: #e3232b;
    --brand-green: #3cb02a;
    --brand-blue: #2f8fd0;
    --title-blue: #3f68c4;
    --divider: #333333;
  }
  * { box-sizing: border-box; margin: 0; padding: 0; }
  html, body {
    width: 1200px;
    height: 900px;
    overflow: hidden;
    background: var(--backdrop);
    font-family: "Tinos", "Times New Roman", serif;
    color: var(--ink);
  }
  .stage {
    position: relative;
    width: 1200px;
    height: 900px;
  }
  .card {
    position: absolute;
    top: 290px;
    width: 540px;
    height: 320px;
    background: var(--card);
    border-radius: 26px;
    box-shadow: 0 6px 18px rgba(0,0,0,0.12);
    overflow: hidden;
  }
  .card--geo { left: 40px; }
  .card--realty { left: 620px; }

  .brand {
    position: absolute;
    left: 0; right: 0; top: 0;
    height: 150px;
    display: flex;
    align-items: center;
    padding-left: 38px;
    gap: 12px;
  }
  .brand__mark { flex: none; }
  .brand__name {
    font-weight: 700;
    font-size: 40px;
    letter-spacing: -0.5px;
    white-space: nowrap;
  }
  .card--geo .brand__name { color: var(--brand-green); }
  .card--realty .brand { padding-left: 60px; gap: 16px; }
  .card--realty .brand__name { color: var(--accent-red); font-size: 38px; }

  .rule {
    position: absolute;
    left: 0; right: 0;
    top: 150px;
    height: 6px;
    background: var(--accent-red);
  }

  .details {
    position: absolute;
    top: 172px;
    left: 0; right: 0;
    display: flex;
  }
  .person {
    width: 230px;
    text-align: right;
    padding-right: 16px;
    padding-top: 22px;
  }
  .card--realty .person { width: 260px; padding-top: 30px; }
  .person__name { font-size: 21px; line-height: 1.15; }
  .person__role {
    font-size: 12px;
    font-style: italic;
    color: var(--title-blue);
    line-height: 1.4;
  }
  .card--realty .person__role { font-size: 16px; }
  .person__phone {
    font-size: 18px;
    color: var(--accent-red);
    margin-top: 3px;
  }
  .contact {
    border-left: 2px solid var(--divider);
    padding-left: 16px;
    height: 118px;
    font-size: 19px;
    line-height: 1.22;
  }
  .contact__gap { margin-top: 10px; }
  .contact__link { color: var(--accent-red); }
  .card--realty .contact { font-size: 16.5px; line-height: 1.28; }
  .contact__address {
    font-size: 14px;
    font-weight: 700;
    margin-top: 8px;
    line-height: 1.3;
  }
</style>
</head>
<body>
<main class="stage">

  <section class="card card--geo">
    <header class="brand">
      <svg class="brand__mark" width="40" height="40" viewBox="0 0 40 40" aria-hidden="true">
        <circle cx="20" cy="20" r="19" fill="var(--brand-green)"/>
      </svg>
      <span class="brand__name">TerraLoopSolar,Inc.com</span>
    </header>
    <div class="rule"></div>
    <div class="details">
      <div class="person">
        <p class="person__name">Daniel Okafor</p>
        <p class="person__role">M.E &amp; Certified Geothermal Installer</p>
        <p class="person__phone">(555) 214-7780</p>
      </div>
      <div class="contact">
        <p>4120 N 87th Ave. # B200</p>
        <p>Lakeview, WA 98555</p>
        <p class="contact__gap">To learn about Geo</p>
        <p>Visit our Website:</p>
        <p class="contact__link">TerraLoopSolarinc.com</p>
      </div>
    </div>
  </section>

  <section class="card card--realty">
    <header class="brand">
      <svg class="brand__mark" width="52" height="52" viewBox="0 0 52 52" aria-hidden="true">
        <rect x="0" y="0" width="52" height="52" rx="6" fill="var(--brand-blue)"/>
      </svg>
      <span class="brand__name">Harbor Realty, Inc.com</span>
    </header>
    <div class="rule"></div>
    <div class="details">
      <div class="person">
        <p class="person__name">Daniel Okafor</p>
        <p class="person__role">Broker</p>
        <p class="person__phone">(555) 214-7780</p>
      </div>
      <div class="contact">
        <p>Phone: (555) 214-7780</p>
        <p>Fax: (555) 736-0418</p>
        <p class="contact__link">HarborRealtyinc.com</p>
        <p class="contact__address">4120 N 87th Ave. # B200<br>Lakeview, WA 98555</p>
      </div>
    </div>
  </section>

</main>
</body>
</html>
```